Stationary Design for Stunning new Logo

I need to envelopes, letterhead, business cards designed to compliment our new logo.

We are a 25 year old printing company going through a brand refresh. All items should have the design extended to both sides for full print ability.

Industry/Entity Type

Printing

Requirements
Must have
• It must utilize the new logo & colors PMS 300 & PMS 295.

```html
<!DOCTYPE html>
<html lang="en">
<head>
<meta charset="utf-8">
<title>Crestprint Business Card</title>
<link href="https://fonts.googleapis.com/css2?family=Arimo:wght@400;700&display=swap" rel="stylesheet">
<style>
  :root {
    --navy: #0b2a5e;
    --navy-deep: #082150;
    --blue: #1565c0;
    --sky: #4d8fd6;
    --paper: #eef0f2;
    --ink: #2a2f36;
    --stage: #d9dcdf;
  }
  * { margin: 0; padding: 0; box-sizing: border-box; }
  html, body { width: 1200px; height: 900px; overflow: hidden; }
  body {
    background: var(--stage);
    font-family: "Arimo", Arial, sans-serif;
    position: relative;
  }
  .card {
    position: absolute;
    top: 295px;
    width: 540px;
    height: 310px;
    box-shadow: 0 6px 18px rgba(0,0,0,0.18);
    overflow: hidden;
  }
  .card--front { left: 40px; background: linear-gradient(135deg, var(--navy) 0%, var(--navy-deep) 100%); }
  .card--back { left: 620px; background: var(--paper); }

  .wordmark {
    position: absolute;
    font-weight: 700;
    letter-spacing: 3px;
    line-height: 1;
    white-space: nowrap;
  }
  .tagline {
    position: absolute;
    font-size: 10.5px;
    letter-spacing: 0.6px;
    text-transform: uppercase;
    white-space: nowrap;
  }
  .card--front .wordmark { left: 44px; top: 112px; font-size: 50px; color: #ffffff; }
  .card--front .tagline { left: 46px; top: 170px; color: #8fb6e6; }
  .card--front .site {
    position: absolute; right: 40px; bottom: 34px;
    font-size: 12px; color: #c9d8ee; letter-spacing: 0.3px;
  }
  .site strong { font-weight: 700; }

  .card--back .brand-dot {
    position: absolute; left: 34px; top: 82px;
    width: 54px; height: 54px; border-radius: 50%;
    background: var(--blue);
  }
  .card--back .wordmark { left: 108px; top: 80px; font-size: 46px; color: var(--navy); }
  .card--back .tagline { left: 110px; top: 133px; color: var(--blue); }

  .contact {
    position: absolute; left: 176px; top: 164px;
    padding-left: 16px;
    border-left: 1px solid var(--sky);
    color: var(--ink);
    font-size: 12px;
    line-height: 1.5;
  }
  .contact .name { font-size: 15px; margin-bottom: 4px; }
  .contact .role { font-size: 11.5px; margin-left: 12px; }
  .contact .label { display: inline-block; width: 14px; }
  .contact .address { margin-top: 6px; }
  .contact .site { color: var(--blue); font-size: 12.5px; margin-top: 2px; }
</style>
</head>
<body>
  <section class="card card--front" aria-label="Business card front">
    <div class="wordmark">CRESTPRINT</div>
    <div class="tagline">Dependable Service • Crisp Results • Honest Rates.</div>
    <div class="site">www.<strong>crestprint</strong>.com</div>
  </section>

  <section class="card card--back" aria-label="Business card back">
    <div class="brand-dot"></div>
    <div class="wordmark">CRESTPRINT</div>
    <div class="tagline">Dependable Service • Crisp Results • Honest Rates.</div>
    <div class="contact">
      <div class="name">Elena Morrow<span class="role">Executive Director</span></div>
      <div><span class="label">T</span>+352 47 20 86 113</div>
      <div><span class="label">F</span>+352 47 20 86 114</div>
      <div><span class="label">E</span>morrow@crestprint.com</div>
      <div class="address">12, Rue des Ateliers, Bertrange, L-2740 Country</div>
      <div class="site">www.<strong>crestprint</strong>.com</div>
    </div>
  </section>
</body>
</html>
```